Nutrient Guild of Columbia Website Creation

Nutrient Guild of Columbia seeks a membership website that is visually dynamic, suitable for all who seek knowledge and inspiration about maximizing their health and wellbeing. see nutrientguildofcolumbia.com

Target Market(s)

Scientists, Media, Medical Professionals, Nutritionists, Public

Industry/Entity Type

Nutrition

Number of Pages Required

5+ page

Font styles to use
Sans Serif

Colors
0355a3
ec1f27

Requirements
Must have
• Large Pictures, full screen
• Areas for video, blog, articles
• Membership sign in/ Public Access
• Easy to Edit/Add Content
• Merchant Ready
• please check out http://greenhearthalliance.org This is what I want it to resemble.
Nice to have
• Red White and Blue but not static, old fashioned, but upbeat.
• Movement - subtle
Should not have
• Should not look Governmental-ish
• Flat look
• Small page
• should not look like the basic site at www.nutrientguildofcolumbia.com

```html
<!DOCTYPE html>
<html lang="en">
<head>
<meta charset="utf-8">
<title>Nutrient Guild of Columbia</title>
<link rel="stylesheet" href="https://fonts.googleapis.com/css2?family=Source+Sans+3:ital,wght@0,400;0,600;0,700;1,400;1,700&family=Roboto+Condensed:wght@400;500&family=Roboto:wght@400;500&display=swap">
<style>
:root{
  --blue:#0355a3;
  --red:#ec1f27;
  --navy:#1b2a5c;
  --grey-icon:#8a8a8a;
  --footer:#2b2b2b;
  --footer-deep:#1e1e1e;
  --field:#555555;
}
*{margin:0;padding:0;box-sizing:border-box}
html,body{width:685px;height:1200px;overflow:hidden;background:#fff}
body{position:relative;font-family:"Source Sans 3",sans-serif;color:#fff}
.abs{position:absolute}

/* header */
.header{left:0;top:0;width:685px;height:95px;background:#fff;border-bottom:1px solid #ddd}
.brand-mark{left:64px;top:4px;width:87px;height:87px;border-radius:50%;background:var(--navy)}
.brand-name{left:160px;top:28px;font-size:18px;font-weight:600;color:var(--navy);white-space:nowrap}
.brand-tag{left:161px;top:51px;font-size:10px;color:#8a8a8a}
.nav{left:160px;top:80px;font-family:"Roboto Condensed",sans-serif;font-size:8.4px;font-weight:500;color:var(--navy);white-space:nowrap;letter-spacing:.1px}
.nav span{margin:0 3px}
.social-top{left:477px;top:14px;display:flex;gap:7.5px}
.social-top i{display:block;width:23px;height:23px;border-radius:50%;background:var(--grey-icon)}
.join-tab{left:507px;top:51px;width:114px;height:44px;background:var(--blue);border-radius:10px 10px 0 0;font-family:"Roboto Condensed",sans-serif;font-size:11px;font-weight:500;display:flex;align-items:center;justify-content:center}

/* hero */
.hero{left:0;top:95px;width:685px;height:268px;background:linear-gradient(100deg,#c8151a 0%,#a81014 30%,#3f7a22 55%,#c21a1a 75%,#d8b8a0 100%)}
.hero-card{left:65px;top:161px;width:379px;height:172px;background:rgba(40,6,12,.88);padding:13px 15px}
.hero-card h1{font-size:22px;font-style:italic;font-weight:700;line-height:1.1;white-space:nowrap}
.hero-card p{margin-top:9px;font-size:7.6px;font-style:italic;line-height:13.3px}
.btn-hero{left:79px;top:284px;width:158px;height:30px;border-radius:6px;background:var(--red);font-size:14px;font-weight:600;display:flex;align-items:center;justify-content:center}

/* about band */
.about-band{left:0;top:363px;width:685px;height:30px;background:var(--blue);text-align:center;font-size:17px;line-height:30px}

/* feature panels */
.panel{top:393px;width:229px;height:334px}
.panel-videos{left:0;background:linear-gradient(#222,#141414)}
.panel-blog{left:228px;background:radial-gradient(circle at 55% 35%,#2c2a4a,#6a4a2a 55%,#c46a1a 85%)}
.panel-articles{left:457px;width:228px;background:radial-gradient(circle at 50% 40%,#2c4a2a,#10200f)}
.play{left:93px;top:500px;width:32px;height:22px;border-radius:5px;background:#000}
.panel-info{top:624px;height:103px;background:rgba(0,0,0,.72)}
.panel-info h2{position:absolute;left:6px;top:8px;font-size:17px;font-weight:400;letter-spacing:-.3px}
.panel-info p{position:absolute;left:7px;top:35px;width:200px;font-family:Roboto,sans-serif;font-size:5.6px;line-height:9px}
.explore{top:692px;width:66px;height:21px;border:1.5px solid var(--blue);background:#fff;color:var(--blue);font-family:Roboto,sans-serif;font-weight:500;font-size:6.8px;display:flex;align-items:center;justify-content:center;gap:4px}
.explore.active{border-color:var(--red);color:var(--red)}
.notch{left:329px;top:714px;width:28px;height:28px;border-radius:50%;background:var(--blue)}

/* mission */
.mission{left:0;top:727px;width:685px;height:199px;background:var(--blue)}
.portrait{left:65px;top:763px;width:127px;height:127px;border-radius:50%;border:4px solid #3f79c0;background:radial-gradient(circle at 50% 40%,#c7a890,#6a4a3e 60%,#d9dde2 62%)}
.mission-text{left:213px;top:757px;width:410px;font-size:11.2px;line-height:18.6px}

/* social band */
.social-band{left:0;top:926px;width:685px;height:96px;background:var(--red)}
.social-title{left:0;top:935px;width:685px;text-align:center;font-size:23px}
.social-row{left:271px;top:981px;display:flex;gap:8px}
.social-row i{display:block;width:23px;height:23px;border-radius:50%;background:#fff}

/* footer */
.footer{left:0;top:1022px;width:685px;height:153px;background:var(--footer)}
.footer-links{left:64px;top:1031px;font-size:8.4px;font-weight:700;display:flex;gap:18px}
.field{height:25px;border-radius:7px;background:var(--field);color:#c7c7c7;font-size:9px;padding-left:11px;display:flex;align-items:center}
.btn{height:30px;border-radius:7px;font-size:14px;font-weight:600;display:flex;align-items:center;justify-content:center}
.signup-title{left:376px;top:1031px;width:250px;font-size:13.4px;font-weight:600;line-height:15.5px}
.bottom-bar{left:0;top:1175px;width:685px;height:25px;background:var(--footer-deep)}
.copyright{left:64px;top:1185px;font-family:Roboto,sans-serif;font-size:5.6px;color:#bbb}
.foot-brand{left:530px;top:1180px;font-size:7.6px;font-weight:700;line-height:8px}
.foot-brand small{display:block;font-size:4.2px;font-weight:400;color:#bbb}
</style>
</head>
<body>

<header class="abs header"></header>
<div class="abs brand-mark"></div>
<div class="abs brand-name">Nutrient Guild of Columbia</div>
<div class="abs brand-tag">A Micronutrient Membership Site</div>
<nav class="abs nav">ABOUT US <span>/</span> CONTACT US <span>/</span> MEMBERSHIP OPPORTUNITIES <span>/</span> SIGN IN <span>/</span> VIDEO LIBRARY</nav>
<div class="abs social-top" aria-label="Social links"><i></i><i></i><i></i><i></i><i></i></div>
<div class="abs join-tab">JOIN US TODAY</div>

<section class="abs hero" role="img" aria-label="Close-up photo of red and green bell peppers with a handwritten quality sign"></section>
<div class="abs hero-card">
  <h1>Food for Micronutrient Thought</h1>
  <p>We are searching for those who would relish the opportunity to shape the direction of the Society as we become the ultimate, evidence-based, central resource for scientists, providers, entrepreneurs, patients, and all interested parties. I am accepting nominations for the 13 Founder's that will become the leaders of the think tank - those accomplished and ready to multiply their efforts through innovation, education, and motivation.</p>
</div>
<div class="abs btn-hero">Join Us Today</div>

<div class="abs about-band">About Nutrient Guild of Columbia</div>

<div class="abs panel panel-videos" role="img" aria-label="Video still of a conference presentation slide"></div>
<div class="abs play"><svg width="32" height="22" viewBox="0 0 32 22"><path d="M13 6 L21 11 L13 16Z" fill="#fff"/></svg></div>
<div class="abs panel panel-blog" role="img" aria-label="Photo of a basket of grapes, walnuts, kiwi and orange"></div>
<div class="abs panel panel-articles" role="img" aria-label="Photo of fresh basil leaves"></div>

<div class="abs panel-info" style="left:0;width:228px">
  <h2>VIDEOS</h2>
  <p>Dr. Warren K. Hale, MD, MPH presented the NEST 2010 Paper at the 10th International Conference, Nutrition &amp; Diagnostics September 4 -7, 2010 in Lindmark, Norvania.</p>
</div>
<div class="abs panel-info" style="left:228px;width:229px;background:rgba(0,0,0,.55)">
  <h2>BLOG</h2>
  <p style="width:225px">Lorem ipsum dolor sit amet consecutor. Lorem ipsum dolor sit amet consecutor.</p>
</div>
<div class="abs panel-info" style="left:457px;width:228px">
  <h2>ARTICLES</h2>
  <p style="width:225px">Lorem ipsum dolor sit amet consecutor. Lorem ipsum dolor sit amet consecutor.</p>
</div>

<div class="abs explore" style="left:154px"><svg width="8" height="8" viewBox="0 0 8 8"><path d="M4 1H1v6h6V4M4.5 1H7v2.5M7 1L3.5 4.5" fill="none" stroke="currentColor" stroke-width="1.2"/></svg>EXPLORE</div>
<div class="abs explore active" style="left:383px"><svg width="8" height="8" viewBox="0 0 8 8"><path d="M4 1H1v6h6V4M4.5 1H7v2.5M7 1L3.5 4.5" fill="none" stroke="currentColor" stroke-width="1.2"/></svg>EXPLORE</div>
<div class="abs explore" style="left:612px"><svg width="8" height="8" viewBox="0 0 8 8"><path d="M4 1H1v6h6V4M4.5 1H7v2.5M7 1L3.5 4.5" fill="none" stroke="currentColor" stroke-width="1.2"/></svg>EXPLORE</div>

<section class="abs mission"></section>
<div class="abs notch"><svg width="28" height="14" viewBox="0 0 28 14"><path d="M10 9 L14 5 L18 9Z" fill="#fff"/></svg></div>
<div class="abs portrait" role="img" aria-label="Portrait photo of the guild founder"></div>
<p class="abs mission-text">NGC – the Nutrient Guild of Columbia’s new official website reflects the core mission – to keep it’s members and the Nation up-to-date with all aspects of vitamin and mineral health. NGC promotes the study of vitamins and minerals, furthers the exchange of research and professional experience between members, and provides scientific articles, topical information, web resources, and referrals for health care specialists in the field. NGC also organizes and participates in national and international events related to the topic. We welcome all interested in the field to join our society.</p>

<section class="abs social-band"></section>
<h2 class="abs social-title" style="font-weight:400">Social Media Connections</h2>
<div class="abs social-row" aria-label="Social links"><i></i><i></i><i></i><i></i><i></i></div>

<footer class="abs footer"></footer>
<div class="abs footer-links"><span>News</span><span>Contact</span><span>Privacy &amp; Terms</span></div>
<div class="abs field" style="left:64px;top:1072px;width:246px">Enter keyword(s)</div>
<div class="abs btn" style="left:64px;top:1105px;width:246px;background:var(--blue)">Search the Site</div>
<div class="abs signup-title">Sign up below for updates and learn about ways to get involved.</div>
<div class="abs field" style="left:374px;top:1072px;width:247px">Please enter your Name</div>
<div class="abs field" style="left:374px;top:1104px;width:247px">Please enter your Email Address</div>
<div class="abs btn" style="left:375px;top:1137px;width:246px;background:var(--red)">Join Our Membership</div>

<div class="abs bottom-bar"></div>
<div class="abs copyright">Copyright © 2015 Nutrient Guild of Columbia</div>
<div class="abs foot-brand">Nutrient Guild of Columbia<small>A Micronutrient Membership Site</small></div>

</body>
</html>
```